Re design current site.

Redesign of the current site. Like current design But I don't own it so I need a custom design similar to the current one. Want the model pictures to be shown off as they currently do on the home page I want to show off contact info make it very noticeable and readable.
Target Market(s)
Males age 30-60
Number of Pages Required
1 page
Requirements
Must have
- Must show off model pictures on the page. Must show contact info easy to read easy to find.

```html
<!DOCTYPE html>
<html lang="en">
<head>
<meta charset="utf-8">
<title>Vesper Models</title>
<link href="https://fonts.googleapis.com/css2?family=Exo+2:wght@500;600;700&family=Michroma&family=Lato:wght@400;700&display=swap" rel="stylesheet">
<style>
:root{
  --black:#0c0c0c;
  --nav:#1e1e1e;
  --accent:#ff3d0f;
  --accent-dark:#d92d05;
  --ink:#1b1b1b;
  --body:#3a3a3a;
  --muted:#8a8a8a;
  --light:#f3f3f3;
  --line:#dcdcdc;
  --white:#ffffff;
  --table-head:#333333;
}
*{box-sizing:border-box;margin:0;padding:0}
html,body{width:1200px;height:3098px;overflow:hidden}
body{font-family:"Lato",Arial,sans-serif;color:var(--body);background:var(--white);font-size:16px}
.wrap{width:1002px;margin:0 auto;position:relative}

/* header */
.site-header{height:128px;background:var(--black)}
.site-header .wrap{display:flex;align-items:center;justify-content:space-between;height:128px}
.brand{display:flex;align-items:center;gap:14px;font-family:"Exo 2",sans-serif;font-weight:600;font-size:42px;color:var(--accent);letter-spacing:1px}
.brand-dot{width:22px;height:22px;border-radius:50%;background:var(--accent)}
.header-contact{display:flex;align-items:center;gap:26px;color:var(--white);font-family:"Exo 2",sans-serif;font-weight:600;font-size:19px}
.header-contact .item{display:flex;align-items:center;gap:14px}
.header-contact .sep{width:1px;height:26px;background:#555}
.circle-icon{width:38px;height:38px;border-radius:50%;background:var(--accent);display:flex;align-items:center;justify-content:center}

/* nav */
.main-nav{height:44px;background:var(--nav)}
.main-nav ul{list-style:none;display:flex;height:44px}
.main-nav li{flex:1;text-align:center;line-height:44px;font-family:"Exo 2",sans-serif;font-weight:700;font-size:13px;color:var(--white);text-transform:uppercase;border-right:1px solid #2d2d2d}
.main-nav li:last-child{border-right:0}
.main-nav li.active{background:var(--accent)}

/* hero */
.hero{position:relative;height:557px}
.hero-photo{position:absolute;inset:0;background:linear-gradient(100deg,#c8bfb5 0%,#d8cbbf 35%,#a48a72 60%,#6b5a4b 100%)}
.hero-tagline{position:absolute;right:99px;top:70px;text-align:right;font-family:"Michroma",sans-serif;font-size:29px;line-height:42px;color:var(--ink)}
.hero-strip{position:absolute;left:0;right:0;bottom:0;height:54px;background:rgba(30,30,30,.72);color:var(--white);text-align:center;line-height:54px;font-family:"Exo 2",sans-serif;font-weight:700;font-size:23px}

/* about */
.about{height:547px;padding-top:46px}
.about .wrap{display:flex;justify-content:space-between}
.about-text{width:644px}
.section-title{font-family:"Exo 2",sans-serif;font-weight:700;font-size:33px;color:var(--ink);text-transform:uppercase}
.section-title span{color:var(--accent)}
.about .rule{width:62px;height:3px;background:var(--accent);margin:14px 0 20px}
.about-text p{font-size:14.5px;line-height:24px;margin-bottom:6px}
.about-text strong.lead{display:block;font-size:16px;color:var(--ink);margin-bottom:6px}
.btn-dark{display:inline-block;background:var(--table-head);color:var(--white);font-family:"Exo 2",sans-serif;font-weight:700;font-size:13px;text-transform:uppercase;padding:11px 19px;margin-top:14px}
.booking{width:303px;background:var(--white);box-shadow:0 4px 14px rgba(0,0,0,.18);align-self:flex-start;margin-top:-6px}
.booking h3{background:var(--accent);color:var(--white);text-align:center;font-family:"Exo 2",sans-serif;font-weight:700;font-size:22px;line-height:58px}
.booking-body{padding:16px 22px 28px}
.booking-body p{font-size:12px;line-height:19px;color:var(--muted);margin-bottom:12px}
.field{height:38px;border:1px solid #e6e6e6;background:#f8f8f8;margin-bottom:9px;font-size:12px;color:var(--muted);line-height:38px;padding:0 12px;display:flex;justify-content:space-between;align-items:center}
.booking .submit{display:block;background:var(--table-head);color:var(--white);text-align:center;font-family:"Exo 2",sans-serif;font-weight:700;font-size:15px;line-height:40px;text-transform:uppercase;margin-top:20px}

/* models */
.models{height:961px;background:var(--light);padding-top:46px}
.center-title{text-align:center}
.center-rule{width:640px;height:1px;background:var(--line);margin:16px auto 32px;position:relative}
.center-rule::after{content:"";position:absolute;left:50%;top:-1px;width:62px;height:3px;background:var(--accent);transform:translateX(-50%)}
.model-grid{display:grid;grid-template-columns:repeat(4,232px);column-gap:24px;row-gap:60px}
.model-card{background:var(--white);border:1px solid #e2e2e2;height:302px}
.model-photo{height:244px;position:relative}
.model-plus{position:absolute;left:50%;bottom:-20px;transform:translateX(-50%);width:40px;height:40px;border-radius:50%;background:var(--ink);display:flex;align-items:center;justify-content:center}
.model-plus.on{background:var(--accent)}
.model-info{text-align:center;padding-top:26px}
.model-name{font-family:"Exo 2",sans-serif;font-weight:700;font-size:19px;color:var(--ink)}
.model-stats{font-size:12.5px;color:var(--body);margin-top:4px}
.view-all{text-align:center;margin-top:35px}
.view-all .btn-dark{margin:0;padding:11px 17px;font-size:13px}

/* rates */
.rates{height:514px;padding-top:44px}
.rates-intro{width:840px;margin:0 auto 28px;text-align:center;font-size:14.5px;line-height:26px}
.rates table{width:758px;margin:0 auto;border-collapse:collapse;border:1px solid #e3e3e3}
.rates th{background:var(--table-head);color:var(--white);font-family:"Exo 2",sans-serif;font-weight:700;font-size:23px;text-align:left;height:62px;padding-left:38px}
.rates td{height:49px;padding-left:38px;font-size:17px;color:var(--body);border-top:1px solid #e3e3e3}
.rates tr:nth-child(even) td{background:#f4f4f4}
.rates th+th,.rates td+td{border-left:1px solid #e3e3e3}

/* footer */
.site-footer{height:295px;background:var(--black);position:relative}
.call-pill{position:absolute;left:384px;top:-9px;width:436px;height:66px;background:var(--accent);color:var(--white);text-align:center;line-height:66px;font-family:"Exo 2",sans-serif;font-weight:700;font-size:28px;box-shadow:0 4px 0 var(--accent-dark)}
.footer-cols{display:flex;padding-top:102px}
.footer-col h4{font-family:"Exo 2",sans-serif;font-weight:700;font-size:16px;color:var(--white);text-transform:uppercase}
.footer-col .frule{width:170px;height:1px;background:#3a3a3a;margin:12px 0 14px;position:relative}
.footer-col .frule::after{content:"";position:absolute;left:0;top:-1px;width:60px;height:3px;background:var(--accent)}
.quick{width:256px}
.quick ul{list-style:none;columns:2;width:170px;column-gap:12px}
.quick li{font-size:13px;color:var(--white);line-height:24px}
.contact{width:240px;color:var(--white)}
.contact .name{font-family:"Exo 2",sans-serif;font-weight:700;font-size:15px;margin-bottom:10px}
.contact .row{display:flex;align-items:center;gap:12px;font-size:13px;line-height:34px}
.newsletter{width:300px;color:var(--white)}
.newsletter .frule{width:238px}
.newsletter p{font-size:12px;line-height:18px;width:150px;margin-bottom:24px}
.subscribe{display:flex;width:265px;height:30px}
.subscribe .email{flex:1;background:var(--white);color:var(--muted);font-size:12px;line-height:30px;padding-left:14px}
.subscribe .go{background:var(--accent);color:var(--white);font-weight:700;font-size:12px;line-height:30px;padding:0 12px;text-transform:uppercase}
.badge{position:absolute;left:954px;top:119px;width:147px;height:125px;background:#c9c4a8;border:3px solid #8b8670}
.copyright{position:absolute;left:0;right:0;bottom:0;height:52px;background:#050505;color:#cfcfcf;text-align:center;line-height:52px;font-size:14px}
</style>
</head>
<body>

<header class="site-header">
  <div class="wrap">
    <div class="brand"><span class="brand-dot"></span>Vesper Models</div>
    <div class="header-contact">
      <div class="item">
        <span class="circle-icon"><svg width="18" height="18" viewBox="0 0 24 24"><path fill="#fff" d="M6.6 10.8a15.1 15.1 0 0 0 6.6 6.6l2.2-2.2a1 1 0 0 1 1-.25 11.4 11.4 0 0 0 3.6.57 1 1 0 0 1 1 1V20a1 1 0 0 1-1 1A17 17 0 0 1 3 4a1 1 0 0 1 1-1h3.5a1 1 0 0 1 1 1c0 1.25.2 2.45.57 3.57a1 1 0 0 1-.25 1z"/></svg></span>
        555-014-2280
      </div>
      <span class="sep"></span>
      <div class="item">
        <span class="circle-icon"><svg width="18" height="14" viewBox="0 0 20 14"><rect x="1" y="1" width="18" height="12" rx="1" fill="none" stroke="#fff" stroke-width="2"/><path d="M1 1l9 7 9-7" fill="none" stroke="#fff" stroke-width="2"/></svg></span>
        hello@vespermodels.com
      </div>
    </div>
  </div>
</header>

<nav class="main-nav">
  <div class="wrap">
    <ul>
      <li class="active">Home</li><li>About Us</li><li>Booking</li><li>Models</li><li>Rates</li><li>Employment</li><li>Links</li>
    </ul>
  </div>
</nav>

<section class="hero">
  <div class="hero-photo" role="img" aria-label="Featured model photo in a bright room"></div>
  <h1 class="hero-tagline">TREAT YOURSELF AND<br>WE'LL TREAT YOU</h1>
  <div class="hero-strip">Please Contact Us About Additional Models Not Posted Publicly!</div>
</section>

<section class="about">
  <div class="wrap">
    <div class="about-text">
      <h2 class="section-title">About <span>Vesper Models</span></h2>
      <div class="rule"></div>
      <strong class="lead">Male &amp; female couple available as well.</strong>
      <strong class="lead">Custom clips and videos available for sale!</strong>
      <p><strong>VesperModels Concierge Service</strong> allows clients to request VesperModels to search for models in the location you plan on traveling to. We will search and find attractive models for the dates requested. We also verify they are interested in the service you expect/request and that the pictures we have are recent and real.</p>
      <p>Are you looking for the best Miami companion services providing incall and outcall serving the Miami, Fort Lauderdale, West Palm Beach &amp; other major city's? If so, then you have come to the right place! With the most beautiful, hot, sexy and sizzling companions in the Miami, Fort Lauderdale &amp; West Palm Beach areas. Click Here to See Our Models!</p>
      <p>we, at VesperModels, can accommodate your dreams &amp; demands for any and all kinds of engagements. Our main goal is to offer you a fully satisfying, warm, and pleasurable...</p>
      <span class="btn-dark">Read More</span>
    </div>
    <aside class="booking">
      <h3>BOOKINGS</h3>
      <div class="booking-body">
        <p>Experience our exemplary service for yourself. Once you book with us, you'll be hooked.</p>
        <div class="field">Choose a Model... <svg width="10" height="6" viewBox="0 0 10 6"><path d="M0 0l5 6 5-6z" fill="#999"/></svg></div>
        <div class="field">Full Name</div>
        <div class="field">Email</div>
        <div class="field">Phone</div>
        <div class="field">Appointment Date <svg width="12" height="12" viewBox="0 0 12 12"><rect x="1" y="2" width="10" height="9" fill="none" stroke="#aaa"/><path d="M1 5h10" stroke="#aaa"/></svg></div>
        <span class="submit">Next Step</span>
      </div>
    </aside>
  </div>
</section>

<section class="models">
  <div class="wrap">
    <h2 class="section-title center-title">Our <span>Models</span></h2>
    <div class="center-rule"></div>
    <div class="model-grid">
      <div class="model-card"><div class="model-photo" role="img" aria-label="Model photo of Lena" style="background:linear-gradient(160deg,#e9c9c6,#c7578a)"><span class="model-plus on"><svg width="14" height="14" viewBox="0 0 14 14"><path d="M7 1v12M1 7h12" stroke="#fff" stroke-width="2.4"/></svg></span></div><div class="model-info"><div class="model-name">Lena</div><div class="model-stats">20 - 5'3 - 120 - 34B</div></div></div>
      <div class="model-card"><div class="model-photo" role="img" aria-label="Model photo of Brooke" style="background:linear-gradient(160deg,#2e2824,#b58a6a)"><span class="model-plus"><svg width="14" height="14" viewBox="0 0 14 14"><path d="M7 1v12M1 7h12" stroke="#fff" stroke-width="2.4"/></svg></span></div><div class="model-info"><div class="model-name">Brooke</div><div class="model-stats">23 - 5'0 - 110 - 34C</div></div></div>
      <div class="model-card"><div class="model-photo" role="img" aria-label="Model photo of Nova Sky" style="background:linear-gradient(160deg,#3f5b2c,#8da06a)"><span class="model-plus"><svg width="14" height="14" viewBox="0 0 14 14"><path d="M7 1v12M1 7h12" stroke="#fff" stroke-width="2.4"/></svg></span></div><div class="model-info"><div class="model-name">Nova Sky</div><div class="model-stats">23 - 5'6 - 110 - 32B</div></div></div>
      <div class="model-card"><div class="model-photo" role="img" aria-label="Model photo of Skye" style="background:linear-gradient(160deg,#3b3a3c,#9c8578)"><span class="model-plus"><svg width="14" height="14" viewBox="0 0 14 14"><path d="M7 1v12M1 7h12" stroke="#fff" stroke-width="2.4"/></svg></span></div><div class="model-info"><div class="model-name">Skye</div><div class="model-stats">21 - 5'5 - 110 - 32C</div></div></div>
      <div class="model-card"><div class="model-photo" role="img" aria-label="Model photo of Dahlia" style="background:linear-gradient(160deg,#5a4a46,#d98aa8)"><span class="model-plus"><svg width="14" height="14" viewBox="0 0 14 14"><path d="M7 1v12M1 7h12" stroke="#fff" stroke-width="2.4"/></svg></span></div><div class="model-info"><div class="model-name">Dahlia</div><div class="model-stats">21 - 5'4 - 130 - 34C</div></div></div>
      <div class="model-card"><div class="model-photo" role="img" aria-label="Model photo of Ruby Vale" style="background:linear-gradient(160deg,#1d1416,#6a2a2c)"><span class="model-plus"><svg width="14" height="14" viewBox="0 0 14 14"><path d="M7 1v12M1 7h12" stroke="#fff" stroke-width="2.4"/></svg></span></div><div class="model-info"><div class="model-name">Ruby Vale</div><div class="model-stats">20 - 5'1 - 90 - 34B</div></div></div>
      <div class="model-card"><div class="model-photo" role="img" aria-label="Model photo of Tessa" style="background:linear-gradient(160deg,#7a3a2a,#caa48a)"><span class="model-plus"><svg width="14" height="14" viewBox="0 0 14 14"><path d="M7 1v12M1 7h12" stroke="#fff" stroke-width="2.4"/></svg></span></div><div class="model-info"><div class="model-name">Tessa</div><div class="model-stats">22 - 5'1 - 95 - 34A</div></div></div>
      <div class="model-card"><div class="model-photo" role="img" aria-label="Model photo of Jade" style="background:linear-gradient(160deg,#d9c2ad,#7a5340)"><span class="model-plus"><svg width="14" height="14" viewBox="0 0 14 14"><path d="M7 1v12M1 7h12" stroke="#fff" stroke-width="2.4"/></svg></span></div><div class="model-info"><div class="model-name">Jade</div><div class="model-stats">21 - 5'3 - 115 - 32B</div></div></div>
    </div>
    <div class="view-all"><span class="btn-dark">View All Models</span></div>
  </div>
</section>

<section class="rates">
  <div class="wrap">
    <h2 class="section-title center-title">Rates</h2>
    <div class="center-rule"></div>
    <p class="rates-intro">We're so glad you're interested in meeting with one of our upscale companions. Here are the donations we request for your entertainment. These rates are non-negotiable.</p>
    <table>
      <tr><th>Time</th><th>Incall</th><th>Outcall</th></tr>
      <tr><td>1 HR</td><td>N/A</td><td>$360</td></tr>
      <tr><td>2 HR</td><td>N/A</td><td>$660</td></tr>
      <tr><td>3 HR</td><td>N/A</td><td>$900</td></tr>
      <tr><td>Over Night</td><td>N/A</td><td>$1,900</td></tr>
    </table>
  </div>
</section>

<footer class="site-footer">
  <div class="call-pill">Contact Us - 555-014-2280</div>
  <div class="wrap">
    <div class="footer-cols">
      <div class="footer-col quick">
        <h4>Quick Links</h4><div class="frule"></div>
        <ul><li>Home</li><li>About Us</li><li>Booking</li><li>Models</li><li>Rates</li><li>Employment</li><li>Links</li></ul>
      </div>
      <div class="footer-col contact">
        <h4>Contact Info</h4><div class="frule"></div>
        <div class="name">VESPER MODELS</div>
        <div class="row"><svg width="14" height="14" viewBox="0 0 24 24"><path fill="#ff3d0f" d="M6.6 10.8a15.1 15.1 0 0 0 6.6 6.6l2.2-2.2a1 1 0 0 1 1-.25 11.4 11.4 0 0 0 3.6.57 1 1 0 0 1 1 1V20a1 1 0 0 1-1 1A17 17 0 0 1 3 4a1 1 0 0 1 1-1h3.5a1 1 0 0 1 1 1c0 1.25.2 2.45.57 3.57a1 1 0 0 1-.25 1z"/></svg>555-014-2280</div>
        <div class="row"><svg width="14" height="10" viewBox="0 0 20 14"><rect width="20" height="14" rx="2" fill="#ff3d0f"/></svg>hello@vespermodels.com</div>
      </div>
      <div class="footer-col newsletter">
        <h4>Join My Newsletter</h4><div class="frule"></div>
        <p>Get The Latest Updates By Entering Your Email Address</p>
        <div class="subscribe"><span class="email">Email Address</span><span class="go">Subscribe</span></div>
      </div>
    </div>
    <div class="badge" role="img" aria-label="Review listing badge"></div>
  </div>
  <div class="copyright">Copyright © 2017 Vesper Models. All Right Reserved</div>
</footer>

</body>
</html>
```